Local electrical company needs two flyers designed

We are a small local electrical contracting company and are in desperate need of a awasome flyer design to help grow our business

hi everyone.

please keep the logo off the front page.
it can go on the rear.

We are really trying to portray a angry/frustrated women BECAUSE her lights are broken.
not light globes

Target Market(s)

Home owners

Industry/Entity Type

Electrical

Font styles to use
Serif

Requirements
Nice to have

```html
<!DOCTYPE html>
<html lang="en">
<head>
<meta charset="utf-8">
<title>Lighting Replacement Flyer</title>
<link rel="stylesheet" href="https://fonts.googleapis.com/css2?family=Gelasio:wght@400;700&family=Carlito:wght@700&display=swap">
<style>
  :root {
    --page: #ffffff;
    --frame: #222222;
    --green-deep: #004329;
    --green-mid: #4a8a2e;
    --green-lime: #b2c90c;
    --tab-green: #009a46;
    --tab-ink: #17261b;
    --cream: #fdf7d8;
    --photo-dark: #2a0a08;
    --photo-red: #6e1510;
    --offer-box: #001b0a;
    --fold: #0f4a37;
    --offer-ink: #dbe27e;
  }
  * { margin: 0; padding: 0; box-sizing: border-box; }
  html, body {
    width: 1200px; height: 840px; overflow: hidden;
    background: var(--page);
  }
  .canvas {
    position: relative; width: 1200px; height: 840px;
    background: var(--page);
    border: 1px solid #9a9a9a;
  }
  .flyer {
    position: absolute; left: 57px; top: 58px; width: 1085px; height: 723px;
    border: 1px solid var(--frame);
    background: linear-gradient(to bottom,
      var(--green-deep) 0%, #1f5e2c 25%, var(--green-mid) 55%,
      #8fb81c 72%, var(--green-lime) 82%, var(--green-lime) 100%);
    overflow: hidden;
    font-family: "Gelasio", Georgia, serif;
    color: var(--cream);
  }
  .service-tab {
    position: absolute; right: 0; top: 0; width: 399px; height: 79px;
    background: var(--tab-green);
    font-family: "Carlito", "Calibri", sans-serif; font-weight: 700;
    font-size: 28px; color: var(--tab-ink);
    display: flex; align-items: center; justify-content: flex-end;
    padding-right: 33px; padding-top: 4px;
  }
  .photo-area {
    position: absolute; left: 591px; top: 167px; width: 494px; height: 366px;
    background: radial-gradient(ellipse at 50% 55%, var(--photo-red) 0%, var(--photo-dark) 70%, #150504 100%);
  }
  .headline {
    position: absolute; font-weight: 400; font-size: 78px; line-height: 1;
    white-space: nowrap;
  }
  .headline-1 { left: 64px; top: 70px; }
  .headline-2 { left: 189px; top: 160px; }
  .subline {
    position: absolute; font-size: 38px; line-height: 1; white-space: nowrap;
    transform: scaleX(0.88); transform-origin: left;
  }
  .subline-1 { left: 68px; top: 278px; }
  .subline-2 { left: 68px; top: 347px; }
  .question {
    position: absolute; left: 63px; top: 415px; font-size: 50px; line-height: 1;
    white-space: nowrap; transform: scaleX(0.9); transform-origin: left;
  }
  .offer-fold { position: absolute; left: 442px; top: 486px; }
  .offer {
    position: absolute; left: 442px; top: 532px; width: 643px; height: 141px;
    background: var(--offer-box); color: var(--offer-ink); font-weight: 700;
  }
  .offer-amount {
    position: absolute; left: 22px; top: 4px; font-size: 84px; line-height: 1;
    white-space: nowrap;
  }
  .offer-detail {
    position: absolute; left: 30px; top: 92px; font-size: 32px; line-height: 1;
    white-space: nowrap;
  }
</style>
</head>
<body>
<div class="canvas">
  <section class="flyer">
    <div class="photo-area" role="img" aria-label="Photo of a frustrated woman clutching her head in a dim red-lit room"></div>
    <div class="service-tab">Lighting replacement</div>
    <h1 class="headline headline-1">Is your lighting</h1>
    <p class="headline headline-2">frustrating you?</p>
    <p class="subline subline-1">Tired of coming home to</p>
    <p class="subline subline-2">lights that don't always work?</p>
    <p class="question">Thinking of a change?</p>
    <svg class="offer-fold" width="66" height="46" viewBox="0 0 66 46" aria-hidden="true">
      <polygon points="0,46 66,0 66,46" fill="var(--fold)"/>
    </svg>
    <div class="offer">
      <p class="offer-amount">SAVE$25 off</p>
      <p class="offer-detail">your lighting replacement</p>
    </div>
  </section>
</div>
</body>
</html>
```